Flyer Design for sewing business

Hi. i need flyers for my new business called " Vora Stitchworks". I am based in Sauchie. I offer Door to Door Clothing Alteration Service!
I provide a door to door alteration service for Clackmannanshire area with 20 miles radiance! (I give free consultations at your preferred location where I can accurately quote the cost of the alteration, as this depends on the garment itself. I aim to deliver the completed item back to you within a week though often it is less than this.)
I also design and sew occasional girls dresses ( first communion, flower girl, party dresses)
The consultation are free with no commitment to take the service.

I wold like see designs that use colors similar to colors on my website, like dusty pink, orange.

To contact either phone MIRA 07912348806
or email: mira.tusk71@quellmail.com

www.brimlink.com/vorastitchworks
www.vora-stitchworks.pagenest.com

THAT IS THE Price List Jeans/Trousers: Shorten....................................from £10.00 Taken in (waist).......................from £8.00 Taken in (side seams)..............from £10.00 Replace zip...............................from £10.00 Dresses/Skirts: Shorten....................................from £10.00 Taken in (waist).......................from £8.00 Taken in (side seams)..............from £8.00 Replace zip...............................from £10.00 Jacket/Coat: Shorten sleeves........................from £12.00 Shorten length (Jacket)...........from £16.00 Shorten length (Coat)..............from £18.00 Taken in (back seam)...............from £12.00 Taken in (side seams)..............from £18.00 Repairs......................................from £5.00 Bridal: Shorten Wedding Dress...........from £25.00 All other bridal alteration quotes can be given on consultation.

Reason: HI, ALL! IN THE NEXT FEW DAYS I GONE EXPERIENCE HOUSE MOVE AND SOME STRESS INVOLVING IN THIS.THANK YOU ALL FOR UNDERSTANDING AND A PATIENCE!

```html
<!DOCTYPE html>
<html lang="en">
<head>
<meta charset="utf-8">
<title>Vora Stitchworks – Door-to-Door Alteration Service</title>
<link rel="stylesheet" href="https://fonts.googleapis.com/css2?family=IM+Fell+English:ital@0;1&family=IM+Fell+English+SC&family=Parisienne&display=swap">
<style>
  :root {
    --cream: #fbf1e6;
    --peach: #f6e0cc;
    --rose: #d96a78;
    --band: #d97681;
    --ink: #2a2020;
    --ink-soft: #4a3a3a;
    --outline: #5b2b33;
    --white: #ffffff;
    --form-light: #f3e7d6;
    --form-mid: #e4d2b9;
    --logo-red: #d2402f;
  }
  * { box-sizing: border-box; margin: 0; padding: 0; }
  html, body { width: 1200px; height: 572px; overflow: hidden; background: var(--cream); }
  .flyer {
    position: relative;
    width: 1200px;
    height: 572px;
    overflow: hidden;
    background: radial-gradient(ellipse at 50% 45%, var(--cream) 0%, var(--peach) 100%);
    font-family: "IM Fell English", "Times New Roman", serif;
    color: var(--ink);
  }

  /* Title ribbon */
  .title-banner { position: absolute; left: 170px; top: 50px; width: 370px; height: 96px; }
  .title-banner svg { position: absolute; inset: 0; }
  .title-kicker {
    position: absolute; left: 0; right: 0; top: 22px;
    text-align: center; font-size: 13px; letter-spacing: 0.3px; color: var(--ink);
    font-family: "IM Fell English SC", "Times New Roman", serif; line-height: 1;
  }
  .title-main {
    position: absolute; left: 0; right: 0; top: 40px;
    text-align: center; font-family: "Parisienne", cursive; font-weight: 400;
    font-size: 29px; color: var(--white); line-height: 1;
  }

  /* Price lists */
  .price-group { position: absolute; }
  .price-group h2 {
    font-family: "IM Fell English SC", "Times New Roman", serif;
    font-style: normal; font-weight: 400;
    font-size: 23px; color: var(--rose); line-height: 1; margin-bottom: 6px;
    transform: skewX(-10deg); transform-origin: left bottom;
  }
  .price-row {
    display: grid; grid-template-columns: 192px auto; align-items: baseline;
    font-size: 16.5px; line-height: 24.6px; white-space: nowrap;
  }
  .price-row em { font-style: italic; }
  .price-row .from { font-size: 12px; margin-right: 5px; }
  .group-jeans   { left: 45px;  top: 196px; }
  .group-dresses { left: 45px;  top: 343px; }
  .group-jacket  { left: 428px; top: 196px; }
  .group-bridal  { left: 428px; top: 392px; }
  .bridal-note { font-style: italic; font-size: 12px; line-height: 15px; color: var(--ink); }

  /* Dress form photo area */
  .dress-form {
    position: absolute; left: 800px; top: 20px; width: 215px; height: 487px;
    background: radial-gradient(ellipse at 50% 40%, var(--form-light) 0%, var(--form-mid) 60%, rgba(228,210,185,0) 78%);
  }

  /* Brand name */
  .brand {
    position: absolute; left: 1036px; top: 442px; width: 140px;
    display: flex; align-items: center; justify-content: center; gap: 7px;
    font-family: "IM Fell English SC", "Times New Roman", serif;
    font-size: 14px; letter-spacing: 0.6px; color: var(--ink-soft); white-space: nowrap;
  }
  .brand-dot { width: 10px; height: 10px; border-radius: 50%; background: var(--logo-red); flex: none; }

  /* Contact band */
  .contact-band {
    position: absolute; left: 0; bottom: 0; width: 1200px; height: 65px;
    background: var(--band);
    display: flex; align-items: center; justify-content: center;
    font-size: 16.5px; color: var(--white); white-space: nowrap;
  }
  .contact-band .item { padding: 0 14px; }
  .contact-band .item + .item { border-left: 1px solid rgba(255,255,255,0.75); }
  .contact-band .label { font-style: italic; }
  .contact-band .site { color: var(--ink); font-weight: 700; letter-spacing: 0.3px; }
</style>
</head>
<body>
<main class="flyer">

  <header class="title-banner">
    <svg viewBox="0 0 370 96" width="370" height="96" aria-hidden="true">
      <path d="M22 20 Q185 6 348 20 L332 48 L348 78 Q185 64 22 78 L38 48 Z"
            fill="var(--rose)" stroke="var(--outline)" stroke-width="2"/>
      <path d="M34 28 Q185 15 336 28" fill="none" stroke="var(--outline)" stroke-width="1"/>
      <path d="M34 70 Q185 57 336 70" fill="none" stroke="var(--outline)" stroke-width="1"/>
    </svg>
    <div class="title-kicker">DOOR-TO-DOOR</div>
    <h1 class="title-main">Alteration Service</h1>
  </header>

  <section class="price-group group-jeans">
    <h2>Jeans/Trousers</h2>
    <div class="price-row"><span>Shorten</span><span><span class="from">from</span>£ 10.00</span></div>
    <div class="price-row"><span>Taken in <em>(waist)</em></span><span><span class="from">from</span>£ 8.00</span></div>
    <div class="price-row"><span>Taken in <em>(side seams)</em></span><span><span class="from">from</span>£ 10.00</span></div>
    <div class="price-row"><span>Replace zip</span><span><span class="from">from</span>£ 10.00</span></div>
  </section>

  <section class="price-group group-dresses">
    <h2>Dresses/Skirts</h2>
    <div class="price-row"><span>Shorten</span><span><span class="from">from</span>£ 10.00</span></div>
    <div class="price-row"><span>Taken in <em>(waist)</em></span><span><span class="from">from</span>£ 8.00</span></div>
    <div class="price-row"><span>Taken in <em>(side seams)</em></span><span><span class="from">from</span>£ 8.00</span></div>
    <div class="price-row"><span>Replace zip</span><span><span class="from">from</span>£ 10.00</span></div>
  </section>

  <section class="price-group group-jacket">
    <h2>Jacket/Coat</h2>
    <div class="price-row"><span>Shorten <em>(sleeves)</em></span><span><span class="from">from</span>£ 12.00</span></div>
    <div class="price-row"><span>Shorten length <em>(Jacket)</em></span><span><span class="from">from</span>£ 16.00</span></div>
    <div class="price-row"><span>Shorten length <em>(Coat)</em></span><span><span class="from">from</span>£ 18.00</span></div>
    <div class="price-row"><span>Taken in <em>(back seam)</em></span><span><span class="from">from</span>£ 12.00</span></div>
    <div class="price-row"><span>Taken in <em>(side seams)</em></span><span><span class="from">from</span>£ 18.00</span></div>
    <div class="price-row"><span>Repairs</span><span><span class="from">from</span>£ 5.00</span></div>
  </section>

  <section class="price-group group-bridal">
    <h2>Bridal:</h2>
    <div class="price-row"><span>Shorten Wedding Dress</span><span><span class="from">from</span>£ 25.00</span></div>
    <p class="bridal-note">All other bridal alteration quotes can be given on consultation.</p>
  </section>

  <div class="dress-form" role="img" aria-label="Photograph of a cream tailor's dress form draped with pink measuring tapes and scissors"></div>

  <div class="brand"><span class="brand-dot"></span><span>Vora Stitchworks</span></div>

  <footer class="contact-band">
    <span class="item"><span class="label">Phone:</span> 07912348806</span>
    <span class="item"><span class="label">Email:</span> mira.tusk71@quellmail.com</span>
    <span class="item">www.brimlink.com/vorastitchworks</span>
    <span class="item site">www.vora-stitchworks.pagenest.com</span>
  </footer>

</main>
</body>
</html>
```